Business Card Design Project for International Business Consultanting Firm

KEPT Global was established in 1998 and most recently updated our logo.
We provide advice and consultation regarding international business deals; we are also business brokers; and consultants to entreprenueurs. Excellence across borders is our slogan.

Our Previous business card we had KEPT Global and under that; Business Brokers, Int'l Consultants, Finance, Travel and Tourism. I think we branded ourselves too broad so i will keep within the scope of Business and Finance Brokers Domestic and International.

We are looking for a design that conveys modern elegance with simplicity, and class as well as communicate safety and stability.

Target Market(s)

International and domestic business people, entrepreneurs and professionals

Industry/Entity Type

Safety

Requirements
Must have
• Both sides of the business card must be designed.

Must include our logo which is attached.

I am open to modern sophisticated elegance.

Be extremely creative.

Include an area for name, title, business address, telephone, email address and website address

The look must be polished and clever
Nice to have
• maybe two-tone business card; one side vs the other

```html
<!DOCTYPE html>
<html lang="en">
<head>
<meta charset="utf-8">
<title>KEPT Global – Business Card</title>
<link rel="stylesheet" href="https://fonts.googleapis.com/css2?family=EB+Garamond:ital,wght@0,400;0,600;1,400&display=swap">
<style>
  :root {
    --backdrop: #bfc7c9;
    --card-white: #ffffff;
    --brand-blue: #1f86cf;
    --tagline-grey: #5b6a70;
    --back-edge: #2389d6;
    --back-core: #0e4d85;
    --name-white: #ffffff;
    --contact-tint: #cfe6f8;
    --mark-light: #e9f2f8;
    --mark-blue: #3a93d6;
    --shadow: rgba(0, 0, 0, 0.45);
  }
  * { box-sizing: border-box; margin: 0; padding: 0; }
  html, body {
    width: 1200px;
    height: 1000px;
    overflow: hidden;
    background: var(--backdrop);
    font-family: "EB Garamond", Garamond, serif;
  }
  .canvas { position: relative; width: 1200px; height: 1000px; }

  .card {
    position: absolute;
    width: 740px;
    height: 422px;
    box-shadow: 4px 4px 5px var(--shadow);
    overflow: hidden;
  }

  /* Front */
  .card-front { left: 25px; top: 88px; background: var(--card-white); }
  .brand-mark {
    position: absolute;
    left: 275px; top: 48px;
    width: 190px; height: 190px;
    border-radius: 50%;
    background: radial-gradient(circle at 62% 30%, var(--mark-light) 0%, #d6e6f1 45%, var(--mark-blue) 100%);
  }
  .brand-name {
    position: absolute;
    left: 0; right: 0; top: 236px;
    text-align: center;
    font-size: 94px;
    font-weight: 400;
    line-height: 1;
    color: var(--brand-blue);
    letter-spacing: 0.5px;
  }
  .tagline {
    position: absolute;
    left: 0; right: 0; top: 332px;
    text-align: center;
    font-size: 33px;
    font-style: italic;
    letter-spacing: 2.4px;
    color: var(--tagline-grey);
  }

  /* Back */
  .card-back {
    left: 438px; top: 527px;
    width: 738px; height: 421px;
    background: radial-gradient(ellipse 300px 240px at 372px 90px, var(--back-core) 0%, #1a6db2 45%, var(--back-edge) 100%);
    color: var(--name-white);
    text-align: center;
  }
  .back-mark {
    position: absolute;
    left: 343px; top: 62px;
    width: 58px; height: 58px;
    border-radius: 50%;
    background: radial-gradient(circle at 60% 30%, var(--mark-light) 0%, #cfe2f0 50%, var(--mark-blue) 100%);
  }
  .holder-name {
    position: absolute; left: 0; right: 0; top: 152px;
    font-size: 35px; font-weight: 600; letter-spacing: 0.5px;
  }
  .holder-title {
    position: absolute; left: 0; right: 0; top: 195px;
    font-size: 33px; font-style: italic; letter-spacing: 0.5px;
  }
  .contact {
    position: absolute; left: 0; right: 0; top: 254px;
    list-style: none;
    font-size: 27px;
    line-height: 23.5px;
    color: var(--contact-tint);
  }
  .contact li:first-child { margin-bottom: 1px; }
</style>
</head>
<body>
<main class="canvas">
  <section class="card card-front" aria-label="Card front">
    <div class="brand-mark" aria-hidden="true"></div>
    <h1 class="brand-name">KEPT Global</h1>
    <p class="tagline">Steady Guidance Beyond Every Frontier</p>
  </section>

  <section class="card card-back" aria-label="Card back">
    <div class="back-mark" aria-hidden="true"></div>
    <p class="holder-name">Name Name Name</p>
    <p class="holder-title">Title Title Title</p>
    <ul class="contact">
      <li>Address Address Address Address</li>
      <li>+44 20 7946 0381</li>
      <li>xxxxxxxxxxx@kept-global.com</li>
      <li>www.kept-global.com</li>
    </ul>
  </section>
</main>
</body>
</html>
```